Amber Orchard (instructional dating book)

Title: Amber Orchard
Subtitle: Where to plant tulips along a crooked brick path
Author: R.K. Tolvane
I'm seeking the title to be central with the subtitle underneath and the author slightly lower and to the left. Perhaps a border or two around the font. I thought the background could look aged (off color and old textured paper) and the background slightly punched into the texture like a typewriter has been used. I imagine it something like an old Pemberworth playbook or 1940s morse code manual. Many thanks!

Target Market(s)

18 to 45 year old single people

Industry/Entity Type

Dating

Font styles to use
Serif

Requirements
Must have
• Text with border or two
Nice to have
• Traditional feel. The book is instructional.
Should not have
• Too much color or flair

```html
<!DOCTYPE html>
<html lang="en">
<head>
<meta charset="utf-8">
<title>Amber Orchard — R.K. Tolvane</title>
<link rel="stylesheet" href="https://fonts.googleapis.com/css2?family=Special+Elite&family=Courier+Prime:wght@700&display=swap">
<style>
  :root {
    --paper-light: #ecc79c;
    --paper-mid: #deaf7f;
    --paper-dark: #c98f5f;
    --ink-brown: #7a3d1c;
    --ink-dark: #3a2214;
    --seed-brown: #9a5628;
    --seed-shadow: rgba(60, 30, 10, 0.35);
    --panel-fill: rgba(233, 190, 145, 0.88);
  }
  html, body {
    margin: 0;
    padding: 0;
    width: 834px;
    height: 1200px;
    overflow: hidden;
  }
  .cover {
    position: relative;
    width: 834px;
    height: 1200px;
    overflow: hidden;
    background:
      radial-gradient(ellipse at 30% 25%, var(--paper-light) 0%, transparent 60%),
      radial-gradient(ellipse at 75% 80%, var(--paper-dark) 0%, transparent 55%),
      linear-gradient(160deg, var(--paper-light) 0%, var(--paper-mid) 55%, var(--paper-dark) 100%);
  }
  .seed {
    position: absolute;
    background: var(--seed-brown);
    border-radius: 40%;
    box-shadow: 6px 8px 10px var(--seed-shadow);
  }
  .seed--a { left: 472px; top: 292px; width: 110px; height: 82px; border-radius: 50%; }
  .seed--b { left: 654px; top: 326px; width: 136px; height: 132px; border-radius: 22%; }
  .seed--c { left: 493px; top: 417px; width: 96px;  height: 60px;  border-radius: 45%; }
  .seed--d { left: 62px;  top: 632px; width: 116px; height: 76px;  border-radius: 35%; }
  .seed--e { left: 240px; top: 668px; width: 136px; height: 131px; border-radius: 24%; }
  .seed--f { left: 55px;  top: 757px; width: 116px; height: 90px;  border-radius: 50%; }

  .title-panel {
    position: absolute;
    left: 78px;
    top: 454px;
    width: 700px;
    height: 222px;
    box-sizing: border-box;
    border: 3px solid var(--ink-brown);
    background: var(--panel-fill);
    padding: 8px;
  }
  .title-panel__inner {
    width: 100%;
    height: 100%;
    box-sizing: border-box;
    border: 2px solid var(--ink-brown);
    display: flex;
    flex-direction: column;
    align-items: center;
    justify-content: center;
    gap: 14px;
  }
  .book-title {
    margin: 0;
    font-family: "Special Elite", "Courier New", monospace;
    font-weight: 400;
    font-size: 70px;
    line-height: 1;
    color: var(--ink-brown);
    letter-spacing: 2px;
  }
  .book-subtitle {
    margin: 0;
    font-family: "Courier Prime", "Courier New", monospace;
    font-weight: 700;
    font-size: 19px;
    color: var(--ink-dark);
  }
  .author {
    position: absolute;
    left: 41px;
    top: 1040px;
    margin: 0;
    font-family: "Courier Prime", "Courier New", monospace;
    font-weight: 700;
    font-size: 26px;
    color: var(--ink-dark);
  }
</style>
</head>
<body>
  <main class="cover">
    <div class="seed seed--a" role="img" aria-label="Illustration of a scattered tulip bulb"></div>
    <div class="seed seed--b" role="img" aria-label="Illustration of a scattered tulip bulb"></div>
    <div class="seed seed--c" role="img" aria-label="Illustration of a scattered tulip bulb"></div>
    <div class="seed seed--d" role="img" aria-label="Illustration of a scattered tulip bulb"></div>
    <div class="seed seed--e" role="img" aria-label="Illustration of a scattered tulip bulb"></div>
    <div class="seed seed--f" role="img" aria-label="Illustration of a scattered tulip bulb"></div>

    <section class="title-panel">
      <div class="title-panel__inner">
        <h1 class="book-title">Amber Orchard</h1>
        <p class="book-subtitle">Where to plant tulips along a crooked brick path</p>
      </div>
    </section>

    <p class="author">R.K. Tolvane</p>
  </main>
</body>
</html>
```